Producer Needs a Movie Poster for a Dramatic Film

We need a movie poster for a new dramatic film called "Past the Lantern".
Synopisis: A young drug addict (cocaine and alcohol), ROSS PENDRY, has hit rock bottom after a continuous downward spiral of alcoholism and drug abuse, leaving him with nothing to live for. His ex-girlfriend left him. His best friend doesn’t want anything to do with him. Unable to rehabilitate himself after multiple attempts, he attempts suicide (Jumping off of a high-rise apartment building).
We want the poster to give the dark feel of the film. It should be serious and personable.
We want the three lead actors to be listed on the top of the poster from left to right (Gregory Lint, Miriam Kessub, Osric Demmelby).
The title of the film, Past the Lantern, should be in the center of the poster.
We want "Coming Soon" centered on the bottom of the poster.

No pictures will be provided for this poster, so be creative and make something special for us to use. We're looking for a variety of good ideas.

We're excited to see what you come up with!

Please, make sure you provide us with files we can easily use. Also, we would like a copy of the film title in a separate file for easy use as well. So, two files total (One with the poster, One with just the film title by itself).

Industry/Entity Type

Movie

Requirements
Must have
• We want the three lead actors to be listed on the top of the poster from left to right (Gregory Lint, Miriam Kessub, Osric Demmelby).
• The title of the film, Past the Lantern, should be in the center of the poster.
• We want "Coming Soon" centered on the bottom of the poster.
• Please, make sure you provide us with files we can easily use. Also, we would like a copy of the film title in a separate file for easy use as well. So, two files total (One with the poster, One with just the film title by itself).
Should not have
• Should not have a person on the poster unless they are unrecognizable and you can't see any characteristics. We can't have someone on the poster who won't be in the movie.
• Don't put each locations that won't be in the film either. It takes place in LOs Angeles. Mostly on a high-rise apartment building rooftop.

```html
<!DOCTYPE html>
<html lang="en">
<head>
<meta charset="utf-8">
<title>Past the Lantern – Poster</title>
<link rel="stylesheet" href="https://fonts.googleapis.com/css2?family=Oswald:wght@400;500;600&display=swap">
<style>
  :root {
    --ink: #050505;
    --shadow: #0d0c0a;
    --sepia-deep: #2a261f;
    --sepia-mid: #6f6656;
    --sepia-light: #b9b09e;
    --title-gold: #b4a47f;
    --credit-white: #ece8e0;
  }
  * { margin: 0; padding: 0; box-sizing: border-box; }
  html, body {
    width: 899px;
    height: 1200px;
    overflow: hidden;
    background: var(--ink);
  }
  .poster {
    position: relative;
    width: 899px;
    height: 1200px;
    background: var(--ink);
    font-family: "Oswald", "Arial Narrow", sans-serif;
    overflow: hidden;
  }
  .poster__backdrop {
    position: absolute;
    inset: 0;
    background:
      radial-gradient(ellipse 120px 420px at 470px 560px, rgba(5,5,5,0.95), rgba(5,5,5,0) 100%),
      radial-gradient(ellipse 170px 260px at 470px 330px, rgba(5,5,5,0.9), rgba(5,5,5,0) 100%),
      radial-gradient(ellipse 260px 600px at 760px 520px, var(--sepia-light), rgba(111,102,86,0) 100%),
      radial-gradient(ellipse 200px 500px at 560px 260px, var(--sepia-mid), rgba(42,38,31,0) 100%),
      linear-gradient(90deg, var(--shadow) 0%, var(--shadow) 24%, var(--sepia-deep) 40%, var(--sepia-mid) 70%, var(--sepia-light) 88%, var(--sepia-mid) 100%);
  }
  .poster__backdrop::after {
    content: "";
    position: absolute;
    inset: 0;
    background: linear-gradient(180deg, rgba(5,5,5,0.35) 0%, rgba(5,5,5,0) 25%, rgba(5,5,5,0) 60%, rgba(5,5,5,0.9) 100%);
  }
  .cast {
    position: absolute;
    top: 26px;
    left: 0;
    width: 100%;
    height: 60px;
  }
  .cast__member {
    position: absolute;
    top: 0;
    width: 220px;
    margin-left: -110px;
    text-align: center;
    color: var(--credit-white);
    line-height: 1;
  }
  .cast__member--one { left: 200px; }
  .cast__member--two { left: 446px; }
  .cast__member--three { left: 690px; }
  .cast__first {
    display: block;
    font-size: 16px;
    font-weight: 500;
    letter-spacing: 2px;
    text-transform: uppercase;
  }
  .cast__last {
    display: block;
    margin-top: 6px;
    font-size: 28px;
    font-weight: 500;
    letter-spacing: 2.5px;
    text-transform: uppercase;
  }
  .title {
    position: absolute;
    top: 402px;
    left: 0;
    width: 100%;
    display: flex;
    justify-content: center;
  }
  .title__block {
    color: var(--title-gold);
    font-size: 138px;
    font-weight: 500;
    line-height: 124px;
    letter-spacing: 2px;
    text-transform: uppercase;
    text-align: left;
  }
  .title__line { display: block; }
  .release {
    position: absolute;
    bottom: 24px;
    left: 0;
    width: 100%;
    text-align: center;
    color: var(--credit-white);
    font-size: 40px;
    font-weight: 500;
    letter-spacing: 1px;
    text-transform: uppercase;
  }
</style>
</head>
<body>
  <main class="poster">
    <div class="poster__backdrop" role="img" aria-label="Blurred sepia photograph of a dark, unrecognisable silhouette walking down a dim hallway"></div>

    <header class="cast">
      <p class="cast__member cast__member--one">
        <span class="cast__first">Gregory</span>
        <span class="cast__last">Lint</span>
      </p>
      <p class="cast__member cast__member--two">
        <span class="cast__first">Miriam</span>
        <span class="cast__last">Kessub</span>
      </p>
      <p class="cast__member cast__member--three">
        <span class="cast__first">Osric</span>
        <span class="cast__last">Demmelby</span>
      </p>
    </header>

    <h1 class="title">
      <span class="title__block">
        <span class="title__line">Past</span>
        <span class="title__line">The</span>
        <span class="title__line">Lantern</span>
      </span>
    </h1>

    <p class="release">Coming Soon</p>
  </main>
</body>
</html>
```